Stationery Design Project

We need a stationary design (business card, logo, letterhead) for a new company called "Brightwell Junctions".
We provide software and consulting services to improve business efficiency & increase team engagement.
We focus on workflow automation, business social networking software and collaboration and communication tools built on mobile platforms.
Updates

Target Market(s)

Business with multi-site,young, mobile workforces e.g Retailers, Hospitality

Industry/Entity Type

Communication

Requirements
Must have
• Letterhead to include;
Business Address: 17 Kelvane St, Marrowby Flats, NSW 2187
ABN : 58 417 620 384

```html
<!DOCTYPE html>
<html lang="en">
<head>
<meta charset="utf-8">
<title>Brightwell Junctions – Business Card</title>
<link href="https://fonts.googleapis.com/css2?family=Open+Sans:wght@400;700&display=swap" rel="stylesheet">
<style>
  :root {
    --teal: #14a093;
    --teal-dark: #0b8a7d;
    --teal-light: #5fc1b5;
    --brown: #3b2b27;
    --card-white: #f4f4f4;
    --card-grey: #e6e6e6;
    --backdrop: #9a9a9a;
  }
  * { box-sizing: border-box; margin: 0; padding: 0; }
  html, body { width: 1200px; height: 720px; overflow: hidden; }
  body {
    background: var(--backdrop);
    font-family: "Open Sans", Arial, sans-serif;
    position: relative;
  }
  .card {
    position: absolute;
    top: 217px;
    width: 500px;
    height: 286px;
    border-radius: 22px;
    overflow: hidden;
    box-shadow: 0 6px 18px rgba(0,0,0,0.25);
  }
  .card-front {
    left: 70px;
    background: linear-gradient(110deg, #ffffff 0%, var(--card-white) 50%, var(--card-grey) 100%);
  }
  .card-back {
    left: 630px;
    background: radial-gradient(ellipse at 35% 35%, var(--teal-light) 0%, var(--teal) 55%, var(--teal-dark) 100%);
  }
  .card-curve { position: absolute; left: 0; bottom: 0; width: 500px; height: 286px; }

  .wordmark {
    position: absolute;
    display: flex;
    align-items: center;
    gap: 10px;
    font-weight: 700;
    color: var(--brown);
    white-space: nowrap;
  }
  .wordmark-dot {
    border-radius: 50%;
    background: var(--brown);
    flex: none;
  }
  .card-front .wordmark { left: 34px; top: 30px; font-size: 22px; }
  .card-front .wordmark-dot { width: 18px; height: 18px; }
  .card-back .wordmark { left: 70px; top: 62px; font-size: 30px; }
  .card-back .wordmark-dot { width: 24px; height: 24px; }

  .person { position: absolute; left: 34px; top: 92px; }
  .person-name { font-size: 20px; font-weight: 700; color: var(--brown); line-height: 1.2; }
  .person-role { font-size: 15px; color: var(--teal); line-height: 1.3; }

  .contact-list {
    position: absolute;
    left: 34px;
    top: 168px;
    list-style: none;
    font-size: 14px;
    color: var(--brown);
    line-height: 1.45;
  }
  .contact-list li { display: flex; align-items: center; gap: 7px; }
  .contact-icon { width: 12px; height: 12px; flex: none; }

  .bullet-row {
    position: absolute;
    left: 104px;
    top: 120px;
    display: flex;
    gap: 28px;
    color: #ffffff;
    font-size: 15px;
    list-style: none;
  }
  .bullet-row li::before { content: "•"; margin-right: 3px; }
  .web-address {
    position: absolute;
    left: 104px;
    top: 160px;
    color: #ffffff;
    font-size: 14px;
    font-weight: 700;
    letter-spacing: 0.3px;
  }
</style>
</head>
<body>

  <section class="card card-front" aria-label="Business card front">
    <svg class="card-curve" viewBox="0 0 500 286" aria-hidden="true">
      <path d="M0 200 C 90 245, 170 270, 260 286 L 0 286 Z" fill="var(--teal)"/>
      <path d="M0 212 C 80 252, 150 274, 220 286 L 0 286 Z" fill="var(--teal-dark)" opacity="0.35"/>
    </svg>

    <div class="wordmark">
      <span class="wordmark-dot"></span>
      <span class="wordmark-name">Brightwell Junctions</span>
    </div>

    <div class="person">
      <p class="person-name">Dana Whitcombe</p>
      <p class="person-role">Director</p>
    </div>

    <ul class="contact-list">
      <li>
        <svg class="contact-icon" viewBox="0 0 12 12" aria-hidden="true">
          <rect width="12" height="12" rx="2" fill="var(--teal)"/>
          <path d="M3.5 2.5 L5 2.5 L5.5 4.5 L4.6 5.2 Q5.4 7 7 7.5 L7.6 6.6 L9.5 7 L9.5 8.6 Q5 9.5 2.8 3.6 Z" fill="#fff"/>
        </svg>
        +61 2 5550 1184
      </li>
      <li>
        <svg class="contact-icon" viewBox="0 0 12 12" aria-hidden="true">
          <rect x="3" y="0.5" width="6" height="11" rx="1.2" fill="var(--teal)"/>
          <rect x="4" y="2" width="4" height="5" fill="#fff"/>
        </svg>
        +61 400 555 271
      </li>
      <li>
        <svg class="contact-icon" viewBox="0 0 12 12" aria-hidden="true">
          <rect x="0.5" y="2.5" width="11" height="7.5" rx="1" fill="var(--teal)"/>
          <path d="M1 3 L6 7 L11 3" stroke="#fff" stroke-width="1" fill="none"/>
        </svg>
        dana.whitcombe@brightwelljunctions.com
      </li>
    </ul>
  </section>

  <section class="card card-back" aria-label="Business card back">
    <svg class="card-curve" viewBox="0 0 500 286" aria-hidden="true">
      <path d="M0 215 C 110 250, 230 276, 330 286 L 0 286 Z" fill="#f2f2f2"/>
    </svg>

    <div class="wordmark">
      <span class="wordmark-dot"></span>
      <span class="wordmark-name">Brightwell Junctions</span>
    </div>

    <ul class="bullet-row">
      <li>bullet text</li>
      <li>bullet text</li>
      <li>bullet text</li>
    </ul>

    <p class="web-address">www.brightwelljunctions.com</p>
  </section>

</body>
</html>
```